website for local kavenda practicioner and yoga teacher trainer

The website should function primarily as:
A place where people can discover Kavenda and book sessions.
A central hub connecting all of my work.
A professional home that reflects my personality and approach.
Website design for Liesbet Oonwerk — Kavenda® Structural Integration practitioner, movement educator, yoga teacher and teacher trainer.
A website that can grow with future projects.
The website should feel: Warm, Human, Invitational, Professional, Accessible, Intelligent, Calm, Clear, Playful, Exploratory, Trustworthy
Avoid: New age aesthetics, Mystical clichés, Excessive spirituality, ”Guru" vibes, Overly clinical design, Corporate wellness branding, Busy layouts
Think: modern, grounded, curious and real.
My work combines three interconnected areas:
1.Bodywork: Touch, structure, awareness and one-on-one support.
2. Movement: Yoga, Pilates and embodied movement.
3. Education: Teacher trainings, workshops and continued learning.
Underlying values:
Curiosity over certainty
Possibility over perfection
Complexity without overwhelm
Science and lived experience together
Exploration rather than dogma
Human beings before methods
The primary goal of the website is to introduce people to Kavenda® Structural Integration and make it easy for them to:
Understand what Kavenda is
Discover whether it might be relevant for them
Learn what to expect from a session
Book an appointment
Booking should always feel visible and easy.
Secondary Goal: Present all other aspects of my work in one coherent place:
Yoga classes
Pilates classes
Teacher trainings
Workshops
Retreats
One-on-one movement sessions
Collaborations with studios
Website Structure
1: HOME
1.1.Hero Section: Large welcoming image
1.2 Two Main Pathways
- Bodywork: Kavenda® Structural Integration
- Movement & Education: Yoga, Pilates, trainings, workshops and retreats
- About Preview: Small introduction with portrait. + Button:
Read More
1.3 Current Events / What's Coming Up: Upcoming trainings, workshops and retreats. (This section should be easy to update)
1.4. Contact / Newsletter: Simple contact information
2: Kavenda® Structural Integration
What is Kavenda?
For whom is it?
What does a session look like?
FAQ
Prices
Booking
Future possibility:
Kaven Movement sessions
3: Movement
- Introductory text.
- Studio Classes (link to “my home base” - > local yoga studio)
- One-to-One Sessions: booking option (this is small; not a key aspect I want to promote)
- Workshops/ Retreats / Teacher Trainings => This section should be flexible and easy to update. Visitors should be able to click into specific offerings.
4. Events
Dynamic page for: Teacher trainings, Retreats, Workshops (see section in movement; here more elaborate)
Each event should contain: Image, Short description, Location, Date, Button for more information. (Linking to hosting studio/location)
5. Work With Me
For studios, organisations and teacher training schools.
Examples: Guest teaching, Workshops, Anatomy, Sequencing, Teacher development , Continuing education -> Clear call-to-action.
Call to action!!=> Book a Session
Prominent button in the navigation.
Footer:
- About Me: Longer biography (6th page)
Personal story and background.
- Testimonials (7th page): Separate page containing testimonials from:
Kavenda clients
Students
Teacher trainees
- Contact: 8th page
Visual Direction
Natural textures. Lots of white space.Editorial feeling.Professional photography.Simple navigation.
Less "wellness influencer.” More:Thoughtful, Contemporary, Timeless, Grounded, Human
Photography should show:
Teaching
Hands-on work
Natural movement
Real interaction
Simplicity
Avoid stereotypical yoga imagery and overly spiritual aesthetics.
Keywords
Warm. Curious. Human. Professional. Embodied. Intelligent. Accessible. Playful. Grounded. Exploratory. Real.
Inspiration / Core Message
Helping people feel more at home in their bodies through touch, movement and education.
The website should communicate that these are not separate services, but different expressions of the same intention:
Bodywork • Movement • Education.
Colours:
light orange/beige: e3d5c4
light orange/off white: f9f7f3
gray azure: 556b78
orange: d07b5a
grey orange: c09f80
dark grey: 3e3e3e
dark gray cyan 2f4f4f
gray green colour: a7c4a0
Fonts: Montserrat and Poppins + raleway
In added documents a try out idea of a website + logo. I will mainly use the logo with diffrent colours (image next to text).
My audience consists of people who want to feel more at home in their bodies and who appreciate a thoughtful, grounded and human approach to movement, touch and education. (30-65yo)
wellbeing
5+ page
- montserrat, poppins, raleway

```html
<!DOCTYPE html>
<html lang="en">
<head>
<meta charset="utf-8">
<title>Liesbet Oonwerk — Kavenda® Structural Integration, Movement &amp; Education</title>
<link href="https://fonts.googleapis.com/css2?family=Playfair+Display:wght@400;500&family=Poppins:wght@300;400;500;600&family=Montserrat:wght@500;600;700&display=swap" rel="stylesheet">
<style>
:root{
  --sand:#e3d5c4;
  --offwhite:#f9f7f3;
  --azure:#556b78;
  --orange:#d07b5a;
  --greyorange:#c09f80;
  --dark:#3e3e3e;
  --cyan:#2f4f4f;
  --green:#a7c4a0;
  --blush:#f4ebe3;
  --line:#e6ddd2;
  --muted:#8a817a;
  --serif:'Playfair Display', Georgia, serif;
  --sans:'Poppins', Arial, sans-serif;
  --label:'Montserrat', Arial, sans-serif;
}
*{box-sizing:border-box;margin:0;padding:0}
html,body{width:1200px;height:4975px;overflow:hidden}
body{background:var(--offwhite);color:var(--dark);font-family:var(--sans);position:relative}
section,header,footer{position:relative;width:1200px}
.abs{position:absolute}
.eyebrow{font-family:var(--label);font-weight:600;font-size:8.5px;letter-spacing:2px;text-transform:uppercase;color:var(--orange)}
.btn{display:inline-flex;align-items:center;justify-content:center;font-family:var(--label);font-weight:600;font-size:9px;letter-spacing:1.4px;text-transform:uppercase;border-radius:5px;text-decoration:none}
.btn-solid{background:var(--orange);color:#fff;box-shadow:0 4px 10px rgba(208,123,90,.25)}
.btn-ghost{background:#fff;border:1px solid #d9d1c8;color:var(--dark)}
.photo{border-radius:14px;box-shadow:0 12px 30px rgba(62,62,62,.18)}
h1,h2,h3{font-family:var(--serif);font-weight:400;color:var(--dark)}

/* nav */
.site-nav{height:52px;border-bottom:1px solid var(--line)}
.brand{left:150px;top:16px;display:flex;align-items:center;gap:8px;font-family:var(--sans);font-size:12px;color:var(--dark)}
.brand i{width:16px;height:16px;border-radius:50%;background:var(--orange);display:block}
.nav-links{left:403px;top:20px;display:flex;gap:30px;font-family:var(--label);font-weight:600;font-size:9px;letter-spacing:1.2px;color:var(--dark)}
.nav-cta{left:927px;top:12px;width:123px;height:27px}

/* hero */
.hero{height:521px}
.hero h1{left:150px;top:96px;font-size:41px;line-height:47px;width:360px}
.hero p.lead{left:150px;top:253px;width:430px;font-size:11.5px;line-height:19px;color:#5c5652;font-weight:300}
.hero .actions{left:150px;top:344px;display:flex;align-items:center;gap:16px}
.hero .actions .btn-solid{width:161px;height:37px}
.link-under{font-family:var(--label);font-weight:700;font-size:9px;letter-spacing:1.2px;color:var(--dark);border-bottom:1px solid var(--dark);padding-bottom:4px}
.ticks{left:150px;top:392px;list-style:none;font-family:var(--label);font-size:8px;letter-spacing:1px;color:#9a928b;line-height:21px;text-transform:uppercase}
.ticks li::before{content:"✓ ";color:var(--green)}
.hero-photo{left:618px;top:50px;width:432px;height:420px;background:linear-gradient(160deg,#8a4b32 0%,#b66a48 40%,#6d4a36 75%,#cdb79d 100%)}

/* band */
.stat-band{height:57px;background:var(--orange);display:flex;justify-content:space-around;align-items:center;padding:0 40px;font-family:var(--label);font-weight:600;font-size:9.5px;letter-spacing:1.6px;color:#fff;text-transform:uppercase}
.stat-band span::before{content:"• ";color:#f3c7b3}

/* pillars */
.pillars{height:375px}
.pillar{background:#fff;border-radius:6px;box-shadow:0 6px 20px rgba(62,62,62,.06);padding:30px 30px}
.pillar .icon{width:22px;height:22px;margin-bottom:18px}
.pillar h3{font-family:var(--label);font-weight:700;font-size:16px;letter-spacing:1.8px;text-transform:uppercase;margin-bottom:12px}
.pillar p{font-family:var(--sans);font-weight:500;font-size:14.5px;line-height:23px;color:var(--dark);width:158px}
.p-body{left:150px;top:60px;width:287px;height:257px}
.p-body h3{color:var(--azure)}
.p-move{left:454px;top:50px;width:290px;height:280px;background:#f4ebe3;box-shadow:0 12px 30px rgba(62,62,62,.14)}
.p-move h3{color:var(--orange)}
.p-move p{width:138px}
.p-edu{left:763px;top:60px;width:287px;height:257px}
.p-edu h3{color:var(--green)}
.badge{left:545px;top:45px;width:107px;height:17px;border-radius:9px;background:var(--orange);color:#fff;font-family:var(--label);font-size:7px;letter-spacing:1px;display:flex;align-items:center;justify-content:center;text-transform:uppercase}

/* philosophy */
.philosophy{height:299px;background:var(--sand);text-align:center;overflow:hidden}
.philosophy .eyebrow{position:absolute;left:0;right:0;top:52px;color:#9b8a78;font-size:7.5px}
.philosophy blockquote{position:absolute;left:0;right:0;top:78px;font-family:var(--serif);font-size:27px;line-height:38px;color:var(--dark)}
.philosophy p{position:absolute;left:0;right:0;top:214px;font-size:10px;line-height:17px;color:#6b625a;font-weight:300}

/* method */
.method{height:440px}
.method-photo{left:150px;top:48px;width:352px;height:342px;background:linear-gradient(135deg,#d9b49a 0%,#b98462 45%,#6e4f3d 100%)}
.method .eyebrow{left:541px;top:73px;color:var(--dark);font-size:7.5px}
.method h2{left:541px;top:100px;font-size:29px}
.benefits{left:541px;top:166px;width:500px;list-style:none}
.benefits li{display:flex;gap:18px;height:30px;margin-bottom:24px}
.benefits .dot{width:30px;height:30px;border-radius:6px;background:#efe9e2;display:flex;align-items:center;justify-content:center;flex-shrink:0}
.benefits strong{display:block;font-weight:500;font-size:11.5px;line-height:15px;color:var(--dark);margin-bottom:2px}
.benefits span{display:block;font-size:9.5px;line-height:13px;color:#77706a;font-weight:300;white-space:nowrap}
.method .btn-solid{left:541px;top:349px;width:152px;height:34px}

/* pathways */
.pathways{height:626px;display:flex}
.pathway{width:600px;height:626px;position:relative;text-align:center;color:#fff}
.pathway.movement{background:linear-gradient(180deg,#9d8a78 0%,#7a6a5c 55%,#3f3934 100%)}
.pathway.education{background:linear-gradient(180deg,#a8a29a 0%,#7e7870 55%,#3d3a36 100%)}
.pathway h2{position:absolute;left:0;right:0;top:478px;color:#fff;font-size:32px}
.pathway p{position:absolute;left:0;right:0;top:530px;font-size:10.5px;color:#eee6dd;font-weight:300}
.pathway .btn{position:absolute;left:226px;top:570px;width:148px;height:30px;background:#fff;color:var(--dark);font-size:8.5px}

/* events */
.events{height:758px}
.events h2{left:150px;top:52px;font-size:30px}
.events .intro{left:150px;top:106px;width:380px;font-size:10px;line-height:18px;color:#6b625a;font-weight:300}
.view-all{left:943px;top:122px;font-family:var(--label);font-weight:700;font-size:9px;letter-spacing:1.2px;color:var(--orange)}
.event-feature{left:150px;top:190px;width:594px;height:512px;background:#f4ebe3;border-radius:14px}
.event-feature .img{position:absolute;left:30px;top:30px;width:533px;height:280px;border-radius:8px;background:linear-gradient(180deg,#cfd9cf 0%,#7f9165 45%,#b59a6e 100%)}
.date-tag{position:absolute;left:22px;top:18px;padding:4px 10px;border-radius:10px;background:var(--orange);color:#fff;font-family:var(--label);font-weight:600;font-size:7px;letter-spacing:1px}
.event-feature .eyebrow{position:absolute;left:30px;top:355px;font-size:7.5px}
.event-feature h3{position:absolute;left:30px;top:376px;font-size:17px;font-weight:500}
.event-feature p{position:absolute;left:30px;top:416px;width:420px;font-size:10px;line-height:18px;color:#6b625a;font-weight:300}
.register{font-family:var(--label);font-weight:700;font-size:8.5px;letter-spacing:1.2px;color:var(--dark)}
.register b{color:var(--orange);font-weight:600}
.event-feature .register{position:absolute;left:30px;top:472px}
.event-card{left:763px;width:287px;height:246px;background:#fff;border-radius:8px;box-shadow:0 6px 20px rgba(62,62,62,.07)}
.event-card .img{position:absolute;left:15px;top:13px;width:257px;height:148px;border-radius:4px}
.event-card .meta{position:absolute;left:15px;top:178px;font-family:var(--label);font-size:7px;letter-spacing:1px;color:#9a928b;text-transform:uppercase}
.event-card h4{position:absolute;left:15px;top:193px;font-weight:500;font-size:11.5px}
.event-card .register{position:absolute;left:15px;top:217px;font-size:8px}
.ev-1{top:190px}.ev-1 .img{background:linear-gradient(90deg,#d8d3cb 0%,#8f877d 50%,#cfc8be 100%)}
.ev-2{top:460px}.ev-2 .img{background:linear-gradient(135deg,#e9e5df 0%,#9b7560 50%,#d9d4cc 100%)}

/* about */
.about{height:527px}
.about-photo{left:150px;top:79px;width:352px;height:362px;background:linear-gradient(180deg,#4d5e32 0%,#7a8650 50%,#d9d2c3 100%)}
.about .eyebrow{left:541px;top:103px;font-size:7.5px}
.about h2{left:541px;top:132px;font-size:29px}
.about .sub{left:541px;top:178px;font-family:var(--label);font-size:7px;letter-spacing:1.3px;color:#9a928b;text-transform:uppercase}
.about .bio{left:541px;top:212px;width:400px;font-size:10px;line-height:18px;color:#6b625a;font-weight:300}
.about .bio p+p{margin-top:18px}
.about .btn-ghost{left:541px;top:378px;width:158px;height:36px}
.signature{left:725px;top:370px;width:104px;height:30px;border-radius:3px;background:#ece6df}
.sign-role{left:725px;top:406px;font-family:var(--label);font-size:6.5px;letter-spacing:1px;color:#b8b0a8}

/* testimonial */
.testimonial{height:497px;background:var(--blush);text-align:center}
.avatar{left:582px;top:78px;width:36px;height:36px;border-radius:6px;background:linear-gradient(180deg,#8c6b56,#c9b09a)}
.testimonial .qmark{position:absolute;left:0;right:0;top:130px;font-family:var(--serif);font-size:26px;color:#e0b9a6}
.testimonial .stars{position:absolute;left:0;right:0;top:176px;color:var(--orange);font-size:13px;letter-spacing:4px}
.testimonial blockquote{position:absolute;left:275px;width:650px;top:194px;font-family:var(--serif);font-size:27px;line-height:37px;color:var(--dark)}
.testimonial .author{position:absolute;left:0;right:0;top:331px;font-family:var(--label);font-weight:600;font-size:8px;letter-spacing:1.5px;color:var(--orange)}
.testimonial .role{position:absolute;left:0;right:0;top:348px;font-family:var(--label);font-size:6.5px;letter-spacing:1px;color:#a8a099}
.arrows{left:562px;top:403px;display:flex;gap:16px}
.arrows span{width:28px;height:28px;border-radius:50%;border:1px solid #d5ccc2;display:flex;align-items:center;justify-content:center;font-size:12px;color:var(--dark)}

/* cta */
.cta{height:308px;text-align:center}
.cta .eyebrow{position:absolute;left:0;right:0;top:58px;font-size:7.5px}
.cta h2{position:absolute;left:0;right:0;top:82px;font-size:36px}
.cta p{position:absolute;left:400px;width:400px;top:148px;font-size:10.5px;line-height:19px;color:#6b625a;font-weight:300}
.cta .actions{position:absolute;left:0;right:0;top:220px;display:flex;justify-content:center;gap:16px}
.cta .btn-solid{width:210px;height:38px}
.cta .btn-ghost{width:243px;height:38px}

/* newsletter */
.newsletter{height:195px;background:#f0ebe4}
.newsletter h2{left:224px;top:64px;font-size:24px}
.newsletter p{left:224px;top:105px;width:310px;font-size:10px;line-height:18px;color:#6b625a;font-weight:300}
.email{left:657px;top:69px;width:190px;height:44px;background:#fff;border:1px solid #ddd4ca;border-radius:5px;font-size:8.5px;color:#9a928b;display:flex;align-items:center;padding-left:20px}
.subscribe{left:858px;top:69px;width:118px;height:44px;background:var(--dark);color:#fff;border-radius:5px}

/* footer */
.site-footer{height:320px;background:var(--offwhite)}
.foot-brand{left:224px;top:45px;font-family:var(--serif);font-size:26px;color:var(--dark)}
.foot-about{left:224px;top:93px;width:210px;font-size:9.5px;line-height:17px;color:#6b625a;font-weight:300}
.socials{left:224px;top:162px;display:flex;gap:12px}
.socials i{width:11px;height:11px;border:1px solid #8a817a;border-radius:50%;display:block}
.socials i+i{border-radius:2px}
.foot-col{top:58px}
.foot-col h5{font-family:var(--label);font-weight:700;font-size:7.5px;letter-spacing:1.3px;color:var(--dark);margin-bottom:14px}
.foot-col li{list-style:none;font-size:9px;color:#6b625a;margin-bottom:10px;font-weight:300}
.c1{left:572px}.c2{left:672px}.c3{left:875px}
.legal{left:224px;top:256px;width:752px;display:flex;justify-content:space-between;font-size:8.5px;color:#6b625a;font-weight:300}
</style>
</head>
<body>

<header class="site-nav">
  <div class="abs brand"><i></i>Liesbet Oonwerk</div>
  <nav class="abs nav-links"><span>BODYWORK</span><span>MOVEMENT</span><span>EDUCATION</span><span>EVENTS</span><span>ABOUT</span></nav>
  <a class="abs btn btn-solid nav-cta">Book Session</a>
</header>

<section class="hero">
  <div class="abs eyebrow" style="left:150px;top:70px">Kavenda® • Movement Education • Bodywork</div>
  <h1 class="abs">Reconnect With The Intelligence Of Your Body</h1>
  <p class="abs lead">Through Kavenda®, movement education, and therapeutic bodywork, discover a more natural way to move, breathe, and live. Release long-held patterns of tension and build lasting resilience from the inside out.</p>
  <div class="abs actions"><a class="btn btn-solid">Book A Session</a><span class="link-under">EXPLORE TRAINING</span></div>
  <ul class="abs ticks"><li>20+ Years of Experience</li><li>Certified Kavenda Practitioner</li><li>Workshops &amp; Retreats Worldwide</li></ul>
  <div class="abs photo hero-photo" role="img" aria-label="Practitioner giving hands-on bodywork to a client lying on a treatment table in a warm, sunlit room"></div>
</section>

<div class="stat-band"><span>20+ Years Experience</span><span>1000+ Clients Guided</span><span>Certified Kavenda® Practitioner</span><span>Workshops International Training</span></div>

<section class="pillars">
  <article class="abs pillar p-body">
    <svg class="icon" viewBox="0 0 24 24" fill="none" stroke="#556b78" stroke-width="1.4"><path d="M8 12V5.5a1.5 1.5 0 0 1 3 0V11M11 10V4a1.5 1.5 0 0 1 3 0v7M14 10V5.5a1.5 1.5 0 0 1 3 0V14c0 4-2.5 7-6 7s-5-2-6.5-5l-1.5-3a1.5 1.5 0 0 1 2.6-1.5L8 13"/></svg>
    <h3>Bodywork</h3>
    <p>Touch, structure and awareness through Kavenda® Structural Integration.</p>
  </article>
  <article class="abs pillar p-move">
    <svg class="icon" viewBox="0 0 24 24" fill="none" stroke="#d07b5a" stroke-width="1.6"><circle cx="12" cy="5" r="2"/><path d="M12 8v6M6 11l6 2 6-2M5 19h14M8 19l4-5 4 5"/></svg>
    <h3>Movement</h3>
    <p>Yoga, Pilates and embodied movement for greater freedom and resilience.</p>
  </article>
  <div class="abs badge">Most Popular</div>
  <article class="abs pillar p-edu">
    <svg class="icon" viewBox="0 0 24 24" fill="none" stroke="#a7c4a0" stroke-width="1.4"><path d="M3 6h7a2 2 0 0 1 2 2v11a2 2 0 0 0-2-2H3zM21 6h-7a2 2 0 0 0-2 2v11a2 2 0 0 1 2-2h7z"/></svg>
    <h3>Education</h3>
    <p>Teacher trainings, workshops and retreats for continued learning.</p>
  </article>
</section>

<section class="philosophy">
  <div class="eyebrow">The Philosophy</div>
  <blockquote>"Human beings are not machines to<br>optimise."</blockquote>
  <p>At the heart of my work is the belief that our bodies are living, adaptable systems of<br>intelligence—not problems to be fixed.</p>
</section>

<section class="method">
  <div class="abs photo method-photo" role="img" aria-label="Close-up of hands working on a client's back during a structural integration session"></div>
  <div class="abs eyebrow">Structural Integration</div>
  <h2 class="abs">What is Kavenda®?</h2>
  <ul class="abs benefits">
    <li><span class="dot"><svg width="12" height="12" viewBox="0 0 24 24" fill="none" stroke="#8a817a" stroke-width="2"><path d="M4 20L20 4M14 4h6v6"/></svg></span><div><strong>Release chronic tension</strong><span>Move with less effort and free yourself from long-held physical patterns.</span></div></li>
    <li><span class="dot"><svg width="12" height="12" viewBox="0 0 24 24" fill="#8a817a"><circle cx="12" cy="12" r="4"/></svg></span><div><strong>Improve alignment</strong><span>Stand and sit more comfortably by reorganizing the fascia in gravity.</span></div></li>
    <li><span class="dot"><svg width="12" height="12" viewBox="0 0 24 24" fill="none" stroke="#8a817a" stroke-width="2"><path d="M2 12s4-7 10-7 10 7 10 7-4 7-10 7S2 12 2 12z"/><circle cx="12" cy="12" r="3"/></svg></span><div><strong>Restore body awareness</strong><span>Feel more connected, confident, and present in your physical form.</span></div></li>
  </ul>
  <a class="abs btn btn-solid">Book A Session</a>
</section>

<section class="pathways">
  <div class="pathway movement" role="img" aria-label="Group movement class stretching in a bright studio with arched windows">
    <h2>Movement</h2>
    <p>Private sessions for ease, strength and embodied awareness.</p>
    <a class="btn">View Schedule</a>
  </div>
  <div class="pathway education" role="img" aria-label="Educator teaching a room of seated workshop participants">
    <h2>Education</h2>
    <p>Workshops and professional training for practitioners and lifelong learners.</p>
    <a class="btn">Explore Courses</a>
  </div>
</section>

<section class="events">
  <h2 class="abs">Gatherings &amp; Trainings</h2>
  <p class="abs intro">Join me for immersive experiences designed to deepen your practice and understanding.</p>
  <span class="abs view-all">VIEW ALL EVENTS</span>
  <article class="abs event-feature">
    <div class="img" role="img" aria-label="Olive grove with a stone farmhouse and people walking on a sunny path"></div>
    <span class="date-tag">SEPT 12-14</span>
    <div class="eyebrow">Tuscany, Italy</div>
    <h3>Movement Retreat — 3 Days in Tuscany</h3>
    <p>A restorative deep-dive into structural awareness and somatic flow amidst the rolling hills of Tuscany. Includes private integration sessions.</p>
    <span class="register">REGISTER INTEREST <b>→</b></span>
  </article>
  <article class="abs event-card ev-1">
    <div class="img" role="img" aria-label="Person sitting cross-legged on a mat in a quiet studio"></div>
    <div class="meta">Oct 2026 — Amsterdam</div>
    <h4>Teacher Training</h4>
    <span class="register">REGISTER INTEREST <b>→</b></span>
  </article>
  <article class="abs event-card ev-2">
    <div class="img" role="img" aria-label="Hands resting on a table during an anatomy workshop"></div>
    <div class="meta">Nov 2026 — Leiden</div>
    <h4>Anatomy Workshop</h4>
    <span class="register">REGISTER INTEREST <b>→</b></span>
  </article>
</section>

<section class="about">
  <div class="abs photo about-photo" role="img" aria-label="Portrait of the practitioner seated on a garden bench"></div>
  <div class="abs eyebrow">About Liesbet</div>
  <h2 class="abs">The Face Behind The Work</h2>
  <div class="abs sub">Certified Kavenda • Movement Educator • 20+ Years of Practice</div>
  <div class="abs bio">
    <p>I am Liesbet, a certified Kavenda® practitioner and movement educator with over 20 years of experience in the field of somatic health.</p>
    <p>My journey began with a personal quest for relief from chronic pain, which led me to the transformative world of structural integration. My work is not about fixing bodies, but creating conditions for greater ease, awareness and possibility.</p>
  </div>
  <a class="abs btn btn-ghost">Read My Story</a>
  <div class="abs signature" role="img" aria-label="Handwritten signature"></div>
  <div class="abs sign-role">FOUNDER &amp; EDUCATOR</div>
</section>

<section class="testimonial">
  <div class="abs avatar" role="img" aria-label="Small client portrait"></div>
  <div class="qmark">“</div>
  <div class="stars">★★★★★</div>
  <blockquote>"Working with Liesbet helped me understand my body in a completely new way. The tension I'd held for years simply dissolved."</blockquote>
  <div class="author">— MARIT D.</div>
  <div class="role">ARCHITECT &amp; WORKSHOP PARTICIPANT</div>
  <div class="abs arrows"><span>←</span><span>→</span></div>
</section>

<section class="cta">
  <div class="eyebrow">Next Steps</div>
  <h2>Start with a Conversation</h2>
  <p>Whether you're seeking relief from pain, improving movement, or exploring professional training, we'll help you find the right next step.</p>
  <div class="actions"><a class="btn btn-solid">Book A Discovery Call</a><a class="btn btn-ghost">View Upcoming Workshops</a></div>
</section>

<section class="newsletter">
  <h2 class="abs">Stay Connected</h2>
  <p class="abs">I only send letters when I have something meaningful to share about workshops and training.</p>
  <div class="abs email">Your Email Address</div>
  <a class="abs btn subscribe">Subscribe</a>
</section>

<footer class="site-footer">
  <div class="abs foot-brand">Liesbet</div>
  <p class="abs foot-about">Helping people reconnect with their bodies through movement, education and structural integration.</p>
  <div class="abs socials"><i></i><i></i></div>
  <div class="abs foot-col c1"><h5>EXPLORE</h5><ul><li>Home</li><li>Kavenda®</li><li>Movement</li><li>Events</li></ul></div>
  <div class="abs foot-col c2"><h5>PRACTICE</h5><ul><li>About</li><li>Contact</li><li>Privacy</li></ul></div>
  <div class="abs foot-col c3"><h5>LOCATION</h5><ul><li>Leiden, Netherlands</li><li>Studio &amp; International</li></ul></div>
  <div class="abs legal"><span>© 2024 Liesbet Oonwerk Movement &amp; Education. All rights reserved.</span><span>Photography by Field &amp; Frame Studio</span></div>
</footer>

</body>
</html>
```